Professional WordPress Website Design & Development for IT Consulting Company (Quennor)

We are an IT consulting company (Quennor) based in Germany and are looking for a professional, modern and scalable WordPress website design INCLUDING full coding (WordPress theme/template).

IMPORTANT:
We do NOT want only a design (eg Photoshop files).
We want a fully working, coded WordPress website that we can host and manage ourselves.

The uploaded files (PowerPoint, HTML, logo) are ONLY for rough orientation.
They do NOT represent the final structure but give an idea of our visual style.

---

## COMPANY STRUCTURE (IMPORTANT)

Currently we operate as:

* Quennor UG (limited liability)

Planned structure:

* Quennor Operations GmbH (main operating company)
* Quennor Holding GmbH
* optionally later: Quennor Capital GmbH

The website should be designed as a scalable group website, but currently focus on the main brand "Quennor".

---

## BUSINESS FOCUS (IMPORTANT)

Our main business is:
→ Managed Services (core focus)

Additional areas:

* IT Infrastructure (VMware, Citrix, Hyper-V)
* Windows Server/Client environments
* Cloud & Hybrid solutions
* Network, Firewall, VPN
* Data center operations, migrations and rollouts

The website should clearly communicate:
→ reliability, scalability, enterprise-level service quality

---

## DESIGN STYLE & VISUAL DIRECTION

We like the design direction from our uploaded PowerPoint.

IMPORTANT:

* We especially like the green checkered/grid-style background with dark/black gradient
* This style should be used as inspiration
* Colors: green + dark/black + modern IT style

Design should be:

* modern
* clean
* professional
* enterprise-level
* trustworthy
* not playful or overloaded

---

## TECHNICAL REQUIREMENTS

* WordPress (self-hosted)
* Full source code delivery (no proprietary lock-in)
* Custom theme or clean reusable theme
* Editable without developer
* Multilingual: German, English, Polish
* SEO-friendly
* Fast performance
* GDPR/DSVO compliant contact form

---

## RESPONSIVE DESIGN & ACCESSIBILITY

Must be optimized for:

* Desktop
* Tablet
* Mobile

Layout must adapt automatically.

Accessibility:

* Clear typography
* Good contrast
* Easy navigation
* Mobile-friendly usability

Mobile experience must be fully functional and professional.

---

## STRUCTURE (NO ONE-PAGE WEBSITE)

We want a structured website with pages and subpages.

MAIN NAVIGATION (HEADER):

* Home
* Managed Services (MAIN FOCUS)
* Services
* Solutions / Expertise
* Projects / News
* Resources
* Careers
* Company
* Contact

SUBNAVIGATION / SUBPAGES (examples):

Managed Services:

* Overview
* Service Models
* SLAs & Support
* Monitoring & Operations

Services:

* VMware
* Citrix
* Hyper-V
* Windows Server / Client
* SCCM / Intune
* Network / Firewall / VPN

Solutions:

* Data Center
* Cloud / Hybrid
* Migration Projects
* Security / Zero Trust

Projects / News:

* Projects
* Opportunities
* Articles

Resources:

* Available Experts
* Freelancer / Partner
* Internal Staff

Careers:

* Open Positions
* Freelancer Opportunities

Company:

* About Us
* Group Structure
* Values
* References

---

## HEADER / FOOTER STRUCTURE

HEADER:

* Sticky header (always visible)
* Main navigation with dropdowns or mega menu
* Clean, structured layout

FOOTER:

* Legal pages (Imprint, Privacy, Terms)
* Contact information
* Possibly quick links
* Consistent across all pages

---

## SPECIAL FEATURES

1. PROJECT / NEWS SYSTEM

* publish projects
* project opportunities
* articles

2. RESOURCE SYSTEM

* freelancers
* partners
* internal staff

With:

* skills
* availability
* role
* location
* language

---

## IMAGES, ICONS & LICENSING

Stock images (eg iStock) may be used as placeholders.

IMPORTANT:

* We will purchase final licenses ourselves
* No Google images or unknown sources

Icons and illustrations are welcome but must be properly licensed.

At delivery:

* Full asset list required (images, icons, sources, licenses)

---

## DELIVERABLES

We expect:

* Fully working WordPress website
* Full source code
* Installation instructions
* Plugin list
* No hidden dependencies
* No forced subscriptions
* Full usage rights

---

## IMPORTANT

We want to pay ONCE and fully own everything.

---

## LANGUAGES

Content will be managed by us:

* German
* English
* Polish

---

## FILES

Uploaded files are only for inspiration.

---

We are looking for a long-term, scalable and professional solution suitable for enterprise customers.
Updates

Additional update regarding interactions, hover effects and animations:

HOVER EFFECTS

We would like to include subtle and modern hover effects across the website:

Cards (eg Open Positions, Projects): → slight green glow on hover → minimal lift effect (approx. 2–4px)

Navigation (header): → hover color should be green (NOT orange)

Footer links (Imprint, Privacy, Terms): → slightly brighter on hover

Social icons (LinkedIn, XING, Gigstrelo): → subtle glow and slight scale on hover

IMPORTANT: All hover effects must be consistent, clean and not exaggerated.

ACTIVE STATE (VERY IMPORTANT)

Navigation elements must clearly show when they are active (current page).

This applies to:

Header navigation footer left

Behavior:

Active links should remain highlighted (eg green color and/or subtle underline) Users should always clearly see which page they are currently on

IMPORTANT: Active and hover states must be visually consistent across the entire website.

ANIMATIONS / MICRO INTERACTIONS

The website should not feel static.

We would like subtle and professional animations, such as:

smooth transitions between elements minimal background movement (very subtle) soft UI interactions

IMPORTANT: No heavy, flashy or distracting animations.

The goal is a high-end, enterprise-level feel.

COUNTERS / KEY METRICS

We want animated key numbers, for example:

150+ clients 10+ years experience 24/7 support 99.9% uptime

Behavior:

numbers should count up when they come into view (on scroll) fast and smoothly (approx. 0. 5–1 seconds) animation should trigger only once

Overall goal: A modern, dynamic and high-quality website with subtle interactions, not a flashy or overloaded design.

Hi everyone,

I have uploaded additional reference files to give you a clearer idea of the direction we are aiming for.

IMPORTANT: These files are only meant as inspiration and guidance – they are NOT strict templates that must be copied 1:1.

What we particularly like:

Dark / black + green design Subtle grid / tech background (as seen in the PowerPoint) Clean, modern and professional enterprise IT style Structured layout (no one-page scrolling) LANGUAGE FLAGS (IMPORTANT UPDATE)

Please adjust the language selection as follows:

Order:

German (DE) English (EN) Polish (PL)

For ENGLISH: We do NOT want a standard flag.

Instead, please create a combined UK/US flag:

Diagonally split design One side showing the UK flag The other side showing the US flag

This should look clean and professional (not playful).

FOOTER (IMPORTANT)

Footer should be:

Minimal and clean (not large or heavy) Positioned at the very bottom

Include:

Legal Notice / Imprint / Privacy Policy / Data Protection / Terms and Conditions / Terms

And: © Quennor UG

Social icons:

LinkedIn XING Gigstrelo

Please remove:

Facebook Twitter Instagram LAYOUT NOTE

Please avoid duplicate sections (eg "About Us" appearing multiple times).

We prefer a clean and structured layout with clear sections.

Thank you very much – looking forward to your designs!

Ich brauche zusätzliche Tage um durchzusehen

Target Market(s)

Enterprise and mid-sized companies, especially in automotive, finance, technology and IT infrastructure environments.

Industry/Entity Type

IT Consulting / Managed Services / Enterprise IT

Coding

Coded - Design and coding required

Font styles to use
Sans Serif

Colors
0094D4
00A9DD
6FCCEA
C7EBF8
E9F6FB
00AB8E
00BBA5
67D7C9
C6EFE9
E9F9F6
59FF00
82FF00
B8FF75
E3FFCB
F4FFEA

Requirements
Must have
• - Fully coded WordPress website (not just design) - Self-hosted, no dependency on designer - Responsive (desktop, tablet, mobile) - Multilingual (German, English, Polish) - Editable without developer - Clean, modern enterprise design - Structured navigation with subpages (no one-page website) - GDPR-compliant contact form - Scalable structure for future company expansion (group structure)
Nice to have
• - Subtle modern animations (not overloaded) - Mega menu or structured dropdown navigation - Clean icon set and optional illustrations - Reusable page templates - Fast loading performance - SEO-friendly structure - Team presentation with profiles (management, internal staff, technical roles) - Integration of social links (LinkedIn, Xing, Gigstrelo)
Should not have
• - No one-page scrolling website - No overly colorful or playful design - No outdated or generic templates - No confusing or complex navigation - No cheap-looking stock-heavy layouts - No dependency on proprietary builders or subscriptions

```html
<!DOCTYPE html>
<html lang="de">
<head>
<meta charset="utf-8">
<title>Quennor – Managed Service Provider</title>
<link href="https://fonts.googleapis.com/css2?family=Poppins:wght@300;400;500;600;700&display=swap" rel="stylesheet">
<style>
:root{
  --bg-deep:#0b1f0c;
  --bg-dark:#11290f;
  --bg-mid:#1d4a14;
  --bg-glow:#2c6a18;
  --card:#173a12;
  --card-dark:#0f240d;
  --line:rgba(130,255,70,.10);
  --lime:#6fe83a;
  --text:#e6f3e0;
  --muted:#b9cdb2;
  --red:#ff4a3a;
  --slate:#2f5a5a;
  --slate-light:#4d7a78;
  --band:#3fa51a;
}
*{box-sizing:border-box;margin:0;padding:0}
html,body{width:1200px;height:3953px;overflow:hidden;background:var(--bg-deep)}
body{font-family:"Poppins",sans-serif;color:var(--text)}
.page{position:relative;width:1200px;height:3953px;overflow:hidden;
  background:
   repeating-linear-gradient(0deg,var(--line) 0 1px,transparent 1px 46px),
   repeating-linear-gradient(90deg,var(--line) 0 1px,transparent 1px 46px),
   radial-gradient(ellipse 70% 30% at 50% 42%,var(--bg-glow),transparent 70%),
   linear-gradient(180deg,var(--bg-mid) 0%,#245c16 40%,#1f5114 70%,var(--bg-dark) 92%);
}
.abs{position:absolute}
.center{left:0;right:0;text-align:center}
.title{font-weight:700;color:var(--lime);letter-spacing:.2px}
/* header */
.header{left:0;top:0;width:1200px;height:72px;z-index:3;display:flex;align-items:center;padding:0 34px 0 50px;background:linear-gradient(180deg,rgba(8,26,10,.85),rgba(8,26,10,.25))}
.brand{display:flex;align-items:center;gap:10px}
.brand-mark{width:28px;height:28px;border-radius:6px;background:var(--slate-light)}
.brand-name{font-size:26px;font-weight:600;color:var(--slate-light);line-height:1}
.nav{display:flex;gap:17px;margin-left:auto;margin-right:30px;font-size:12px;color:var(--text)}
.nav a{color:inherit;text-decoration:none}
.nav .active{color:var(--lime);text-decoration:underline;text-underline-offset:4px}
.lang{display:flex;align-items:center;gap:5px;font-size:11px;margin-right:30px}
.lang i{width:12px;height:12px;border:1px solid var(--text);border-radius:50%;display:inline-block}
.btn{display:inline-block;background:var(--slate);color:#fff;font-size:11px;font-weight:600;letter-spacing:.4px;text-transform:uppercase;border-radius:4px;padding:9px 20px;border:1px solid rgba(255,255,255,.12)}
/* hero */
.hero-photo{left:0;top:0;width:1200px;height:580px;background:radial-gradient(ellipse 40% 50% at 25% 55%,rgba(60,110,60,.55),transparent),radial-gradient(ellipse 40% 60% at 80% 30%,rgba(50,120,70,.5),transparent),linear-gradient(180deg,#143a1a,#1e4a22 60%,#184020)}
.eyebrow{font-size:10px;font-weight:500;letter-spacing:.4px}
.hero-title{font-size:42px;line-height:49px}
.hero-text{font-size:13px;line-height:17px;color:var(--text)}
/* cards */
.box{background:rgba(15,40,12,.72);border:1px solid rgba(140,255,90,.08);border-radius:6px}
.box-solid{background:var(--card-dark);border-radius:8px}
.h2{font-size:24px;line-height:31px}
.sub{font-size:11px;line-height:15px;color:var(--text)}
.list{list-style:none;font-size:11.5px;line-height:23.5px}
.list li{display:flex;align-items:center;gap:8px}
.dot{width:10px;height:10px;border-radius:50%;flex:none}
.card-title{font-size:15px;font-weight:500;color:var(--lime);margin:20px 0 8px}
.card-text{font-size:10.5px;line-height:15px;color:var(--text)}
.icon{stroke:var(--lime);fill:none;stroke-width:1.6}
.stat-num{font-size:24px;font-weight:600;color:var(--lime)}
.stat-lbl{font-size:10px;letter-spacing:.3px}
.feat{display:flex;gap:22px;padding:24px 26px}
.feat h4{font-size:15px;font-weight:500;color:var(--lime);margin-bottom:6px}
.client{background:#fff;border-radius:3px;display:flex;align-items:center;justify-content:center;font-size:24px;font-weight:600;color:#1d3640}
.label{font-size:9.5px;font-weight:600;letter-spacing:.3px}
.field{background:#10230e;border:1px solid rgba(255,255,255,.08);border-radius:3px;font-size:10px;color:#6f806b;padding:8px 12px}
.foot-col{font-size:11.5px;line-height:21px}
.social{width:14px;height:14px;border-radius:50%;background:var(--lime)}
</style>
</head>
<body>
<div class="page">

  <!-- Hero -->
  <div class="abs hero-photo" role="img" aria-label="Foto: IT-Team vor Monitoring-Bildschirmen im Rechenzentrum"></div>

  <header class="abs header">
    <div class="brand"><span class="brand-mark"></span><span class="brand-name">Quennor</span></div>
    <nav class="nav">
      <a class="active">Home</a><a>Managed Services</a><a>Services</a><a>Solutions</a><a>Projects</a><a>Resources</a><a>Careers</a><a>Company</a><a>Company</a>
    </nav>
    <div class="lang"><i></i>En ⌄</div>
    <span class="btn">Contact</span>
  </header>

  <p class="abs center eyebrow" style="top:173px">MANAGED SERVICE PROVIDER</p>
  <h1 class="abs center title hero-title" style="top:205px">Ihre Externe IT-Abteilung.<br>Proaktiv. Verlässlich.</h1>
  <p class="abs center hero-text" style="top:314px">Keine Kurzfristigen Projekte Mehr. Wir Managen Ihre Gesamte IT-<br>Infrastruktur – Vom Netzwerk Bis Zum Hardware-Lifecycle. Planbarkeit<br>Für Die Nächsten Jahre.</p>
  <div class="abs center" style="top:387px;display:flex;justify-content:center;gap:10px">
    <span class="btn">Jetzt beraten lassen</span><span class="btn">Lösungen</span>
  </div>

  <svg class="abs" style="left:0;top:520px" width="1200" height="150" viewBox="0 0 1200 150" aria-hidden="true">
    <polygon points="0,95 1200,20 1200,60 0,140" fill="#3d6b63"/>
    <polygon points="0,140 1200,60 1200,150 0,150" fill="#1f5114"/>
    <polygon points="330,118 1200,22 1200,80 780,88" fill="var(--band)"/>
    <polygon points="880,86 1200,40 1200,80" fill="#56c426"/>
  </svg>

  <!-- Chaos -->
  <h2 class="abs center title h2" style="top:690px">Schluss Mit IT-Chaos</h2>
  <p class="abs center sub" style="top:727px">Verabschieden Sie Sich Vom Projekt-Denken. Wir Bieten Langfristige Stabilität<br>(3-5 Jahre) Statt Kurzfristiger Fixes.</p>
  <div class="abs box" style="left:289px;top:780px;width:622px;height:157px;display:flex">
    <div style="flex:1;padding:18px 18px">
      <p style="font-size:12px;font-weight:500;color:var(--red);margin-bottom:6px">Ohne Managed Service</p>
      <ul class="list"><li><span class="dot" style="background:var(--red)"></span>Ungeplante Ausfälle</li><li><span class="dot" style="background:var(--red)"></span>Reaktive Problemlösung</li><li><span class="dot" style="background:var(--red)"></span>Unklare Kosten</li><li><span class="dot" style="background:var(--red)"></span>Veraltete Hardware</li></ul>
    </div>
    <div style="flex:1;padding:18px 18px;border-left:1px solid rgba(255,255,255,.08)">
      <p style="font-size:12px;font-weight:500;color:var(--lime);margin-bottom:6px">Mit Quennor Managed IT</p>
      <ul class="list"><li><span class="dot" style="background:var(--lime)"></span>Proaktives Monitoring 24/7</li><li><span class="dot" style="background:var(--lime)"></span>Vorhersehbare Wartung</li><li><span class="dot" style="background:var(--lime)"></span>Fixe Monatskosten</li><li><span class="dot" style="background:var(--lime)"></span>Moderne Infrastruktur</li></ul>
    </div>
  </div>

  <!-- Services -->
  <h2 class="abs center title h2" style="top:1020px">Alles, Was Sie Brauchen.</h2>
  <p class="abs center sub" style="top:1057px">Wir Übernehmen Die Komplexität, Damit Sie Sich Auf Ihr Geschäft Konzentrieren<br>Können. Komplette Abdeckung Von Der Steckdose Bis Zur Cloud.</p>
  <div class="abs box-solid" style="left:156px;top:1114px;width:887px;height:280px;overflow:hidden;border:2px solid #0a1a09">
    <div class="abs" style="left:0;top:0;width:433px;height:280px;background:linear-gradient(135deg,#5f8f55,#3d6a3c 55%,#2c4f2e)" role="img" aria-label="Foto: Beratungsteam bespricht Projekt am Laptop"></div>
    <div class="abs" style="left:472px;top:28px;width:380px">
      <h3 style="font-size:17px;font-weight:500;color:var(--lime)">Full Lifecycle Management</h3>
      <p class="card-text" style="margin-top:12px">Wir Übernehmen Beschaffung, Einrichtung, Wartung Und Fachgerechtes Recycling. Ihr Team Arbeitet Immer Mit Moderner Hardware.</p>
    </div>
    <div class="abs" style="left:472px;top:142px;display:grid;grid-template-columns:175px 175px;row-gap:14px;font-size:13px;color:var(--lime)">
      <div style="display:flex;align-items:center;gap:14px"><span style="width:44px;height:44px;border-radius:6px;background:#1c3a18"></span>Beschaffen</div>
      <div style="display:flex;align-items:center;gap:14px"><span style="width:44px;height:44px;border-radius:6px;background:#1c3a18"></span>Einrichten</div>
      <div style="display:flex;align-items:center;gap:14px"><span style="width:44px;height:44px;border-radius:6px;background:#1c3a18"></span>Warten</div>
      <div style="display:flex;align-items:center;gap:14px"><span style="width:44px;height:44px;border-radius:6px;background:#1c3a18"></span>Recyceln</div>
    </div>
  </div>

  <div class="abs box" style="left:156px;top:1423px;width:276px;height:198px;padding:20px 18px">
    <svg width="40" height="40" viewBox="0 0 40 40" class="icon"><rect x="4" y="6" width="22" height="7" rx="2"/><rect x="4" y="16" width="22" height="7" rx="2"/><rect x="4" y="26" width="14" height="7" rx="2"/><path d="M28 22l8 3v6c0 4-4 6-8 7-4-1-8-3-8-7v-6z"/></svg>
    <h3 class="card-title">Netzwerk-Sicherheit</h3>
    <p class="card-text">Firewall-Management, Regelmäßige Sicherheits-Audits Und VPN-Konfiguration – Ihre Daten Bleiben Geschützt.</p>
  </div>
  <div class="abs box" style="left:460px;top:1423px;width:278px;height:198px;padding:20px 18px">
    <svg width="40" height="40" viewBox="0 0 40 40" class="icon"><circle cx="20" cy="20" r="15" stroke-dasharray="70 10"/><text x="20" y="24" font-size="10" text-anchor="middle" fill="#6fe83a" stroke="none" font-family="Poppins,sans-serif">24/7</text></svg>
    <h3 class="card-title">24/7 Monitoring</h3>
    <p class="card-text">Wir Überwachen Server-Gesundheit, Uptime Und Anomalien. Probleme Erkennen Wir, Bevor Sie Ihren Workflow Beeinträchtigen.</p>
  </div>
  <div class="abs box" style="left:765px;top:1423px;width:278px;height:198px;padding:20px 18px">
    <svg width="40" height="40" viewBox="0 0 40 40" class="icon"><path d="M6 16a20 20 0 0 1 28 0M11 21a13 13 0 0 1 18 0M16 26a6 6 0 0 1 8 0"/><circle cx="20" cy="30" r="1.5" fill="#6fe83a"/></svg>
    <h3 class="card-title">Managed Connectivity</h3>
    <p class="card-text">Stabiles Wi-Fi, Redundante Internet-Verbindungen Und Sichere Office-Netzwerke. Wir Kümmern Uns Um Konfiguration Und Monitoring – Ihr Team Bleibt Ohne Unterbrechungen Verbunden.</p>
  </div>

  <!-- Partnerships -->
  <h2 class="abs title h2" style="left:156px;top:1745px">Langfristige Partnerschaften<br>Statt Einzelprojekte</h2>
  <p class="abs sub" style="left:156px;top:1822px;width:400px">Quennor UG (Haftungsbeschränkt) Ist Ihr Verlässlicher Partner Für Managed IT Services In Deutschland Und Der Schweiz. Wir Denken In Verträgen Von 3-5 Jahren – Nicht In Kurzfristigen Projekten.</p>
  <div class="abs" style="left:156px;top:1906px;display:flex;gap:56px">
    <div><div class="stat-num">3-5 Jahre</div><div class="stat-lbl">VERTRAGSLAUFZEITEN</div></div>
    <div><div class="stat-num">24/7</div><div class="stat-lbl">VERFÜGBARKEIT</div></div>
    <div><div class="stat-num">100%</div><div class="stat-lbl">MADE IN DACH</div></div>
  </div>
  <div class="abs" style="left:612px;top:1711px;width:431px;height:262px;border-radius:4px;background:radial-gradient(ellipse 50% 45% at 50% 55%,#b9c98a,#6e8f52 55%,#2e5a2a)" role="img" aria-label="Illustration: Handschlag zweier Partner vor digitalem Netzwerk"></div>

  <div class="abs box feat" style="left:156px;top:2014px;width:433px;height:127px">
    <svg width="40" height="40" viewBox="0 0 40 40" class="icon" style="flex:none;margin-top:14px"><path d="M4 18l8-8 8 6 8-6 8 8-12 12-4-4-4 4z"/></svg>
    <div><h4>Langfristige Partnerschaften</h4><p class="card-text">Wir Machen Keine Kurz-Projekte. Unsere 3-5 Jahres-Verträge Sorgen Für Stabilität Und Ermöglichen Uns, Ihr Geschäft Wirklich Zu Verstehen.</p></div>
  </div>
  <div class="abs box feat" style="left:611px;top:2014px;width:432px;height:127px">
    <svg width="40" height="40" viewBox="0 0 40 40" class="icon" style="flex:none;margin-top:14px"><circle cx="20" cy="18" r="9"/><path d="M16 30h8M17 34h6M20 4v3M7 18H4M36 18h-3M10 8l2 2M30 8l-2 2"/></svg>
    <div><h4>Proaktiver Ansatz</h4><p class="card-text">Wir Lösen Probleme, Bevor Sie Sie Beeinträchtigen. Unsere Monitoring-Systeme Erkennen Und Beheben Issues Automatisch.</p></div>
  </div>
  <div class="abs box feat" style="left:156px;top:2168px;width:433px;height:127px">
    <svg width="40" height="40" viewBox="0 0 40 40" class="icon" style="flex:none;margin-top:14px"><circle cx="16" cy="12" r="6"/><path d="M5 34c0-7 5-12 11-12s11 5 11 12zM28 20l6 0 0 6"/></svg>
    <div><h4>Deutsche Ingenieurskunst</h4><p class="card-text">Präzision, Zuverlässigkeit Und Liebe Zum Detail. Unser Team Bringt Höchste IT-Standards In Ihre Infrastruktur.</p></div>
  </div>
  <div class="abs box feat" style="left:611px;top:2168px;width:432px;height:127px">
    <svg width="40" height="40" viewBox="0 0 40 40" class="icon" style="flex:none;margin-top:14px"><path d="M20 36s11-11 11-20a11 11 0 0 0-22 0c0 9 11 20 11 20z"/><circle cx="20" cy="16" r="4"/></svg>
    <div><h4>Lokale Präsenz</h4><p class="card-text">Mit Sitz In Deutschland Und Abdeckung Über DE Und CH. Wir Verstehen Lokale Vorschriften Und Compliance-Anforderungen.</p></div>
  </div>

  <!-- About -->
  <div class="abs box" style="left:259px;top:2386px;width:681px;height:236px;text-align:center;padding:44px 40px">
    <h2 class="title h2">Quennor UG<br>(Haftungsbeschränkt)</h2>
    <p class="sub" style="margin-top:20px">Gegründet Von IT-Professionals, Die Vom Traditionellen "Projektbasierten" IT-Service-Modell Frustriert Waren. Quennor Wurde Geschaffen, Um Unternehmen Eine Echte Externe IT-Abteilung Zu Bieten. Wir Fokussieren Uns Auf Planbarkeit, Stabilität Und Langfristigen Wert – Und Ersetzen Das Chaos Mehrerer Dienstleister Durch Eine Verlässliche Partnerschaft.</p>
  </div>

  <!-- Clients -->
  <h2 class="abs center title h2" style="top:2710px">Vertraut Von Unternehmen In Deutschland<br>Und Der Schweiz</h2>
  <div class="abs" style="left:306px;top:2801px;display:flex;gap:20px">
    <div class="client" style="width:191px;height:82px">Arvelo</div>
    <div class="client" style="width:191px;height:82px">Corvanta</div>
    <div class="client" style="width:191px;height:82px">Stratalis</div>
    <div class="client" style="width:191px;height:82px">Transyn</div>
  </div>

  <!-- Contact -->
  <div class="abs box-solid" style="left:156px;top:2977px;width:887px;height:527px;overflow:hidden">
    <div class="abs" style="left:0;top:0;width:409px;height:527px;background:linear-gradient(160deg,#6e9a62,#4b7b45 50%,#2e5530)" role="img" aria-label="Foto: Support-Mitarbeiter mit Headset am Arbeitsplatz"></div>
    <h2 class="abs title h2" style="left:456px;top:64px">Professionelle IT<br>Beginnt Hier.</h2>
    <p class="abs sub" style="left:456px;top:134px;width:360px">Hinterlassen Sie Ihre Kontaktdaten Und Wir Melden Uns Für Ein Unverbindliches Erstgespräch.</p>
    <span class="abs label" style="left:456px;top:190px">NAME</span>
    <span class="abs label" style="left:656px;top:190px">UNTERNEHMEN</span>
    <div class="abs field" style="left:456px;top:204px;width:185px">Max Mustermann</div>
    <div class="abs field" style="left:656px;top:204px;width:186px">Beispiel GmbH</div>
    <span class="abs label" style="left:456px;top:253px">E-MAIL</span>
    <div class="abs field" style="left:456px;top:270px;width:386px">max@firma.example</div>
    <span class="abs label" style="left:456px;top:322px">NACHRICHT</span>
    <div class="abs field" style="left:456px;top:338px;width:386px;height:74px">Erzählen Sie uns von Ihrem IT-Infrastrukturbedarf...</div>
    <span class="abs btn" style="left:456px;top:444px">Beratung anfragen</span>
  </div>

  <svg class="abs" style="left:0;top:3560px" width="1200" height="145" viewBox="0 0 1200 145" aria-hidden="true">
    <polygon points="0,40 1200,70 1200,145 0,145" fill="var(--bg-deep)"/>
    <polygon points="0,40 700,58 1200,20 1200,70 0,140" fill="var(--band)"/>
    <polygon points="0,100 1200,70 1200,145 0,145" fill="var(--bg-deep)"/>
  </svg>

  <!-- Footer -->
  <footer class="abs" style="left:0;top:3700px;width:1200px;height:253px;background:var(--bg-deep)">
    <div class="abs brand" style="left:156px;top:80px"><span class="brand-mark"></span><span class="brand-name">Quennor</span></div>
    <p class="abs" style="left:156px;top:126px;font-size:10px;line-height:15px;width:250px">(Limited Liability)<br>Ihr Verlässlicher Managed Service Provider Für Deutschland Und Die Schweiz.</p>
    <div class="abs foot-col" style="left:491px;top:72px">Leistungen<br>Lifecycle Management<br>Netzwerk-Sicherheit<br>24/7 Monitoring</div>
    <div class="abs foot-col" style="left:717px;top:72px">Unternehmen<br>Über Uns</div>
    <div class="abs foot-col" style="left:909px;top:72px">Rechtliches<br>Impressum<br>Datenschutz<br>AGB</div>
    <div class="abs" style="left:0;top:218px;width:1200px;height:35px;background:#2d5a55;display:flex;align-items:center;padding:0 40px 0 156px;font-size:10px">
      <span>© 2026 Quennor UG. Alle Rechte vorbehalten.</span>
      <span style="margin-left:auto;display:flex;gap:14px" aria-label="Social Media"><i class="social"></i><i class="social"></i><i class="social"></i><i class="social"></i></span>
    </div>
  </footer>

</div>
</body>
</html>
```